Brightvale Cherries Rainier POS Card 7"H x 11"W

We are wanting to create a one-sided 7 x 11 Rainier cherry card that is eye catching and informative.This should be clear and easy to read and not cluttered. We use these cards as a display in grocery stores, demo stands, and other events to market Brightvale Rainier Cherries. We have a few facts that we would like displayed on the card (see below).

Target Market(s)

Consumers

Industry/Entity Type

Agriculture

Font styles to use
Sans Serif

Requirements
Must have
• Yellow cherries - yellow fruit (the blush on the skin is a kiss from the sun)
• Juice doesn't stain - Kid Friendly
• Add contrast to your summer table
• Sweetest Variety - still low glycemic
• Source of Vitamin C, Source of Potassium, and Source of Melatonin
• Rainiers take up to 4x as much work as red cherries
• Natural Color palettes
• Easy to read
• Brightvale Cherries
Nice to have
• Unique, creative, realistc Rainier cherry designs
Should not have
• pastel or neon color scheme, overly cutesy elements

```html
<!DOCTYPE html>
<html lang="en">
<head>
<meta charset="utf-8">
<title>Brightvale Rainier Cherries – Taste the Difference</title>
<link href="https://fonts.googleapis.com/css2?family=Marcellus&family=Lato:wght@400;700&display=swap" rel="stylesheet">
<style>
  :root {
    --cherry-red: #e8432c;
    --band-orange: #ee5a2f;
    --band-deep: #e2442a;
    --ink: #3b3b3b;
    --paper: #ffffff;
    --fruit-yellow: #f7cf5a;
    --fruit-blush: #ef6a45;
    --bowl-red: #9e1f14;
  }
  html, body {
    margin: 0;
    padding: 0;
    overflow: hidden;
    background: var(--paper);
  }
  .card {
    position: relative;
    width: 1200px;
    height: 765px;
    overflow: hidden;
    background: var(--paper);
    font-family: "Lato", sans-serif;
  }
  .card__art {
    position: absolute;
    inset: 0;
  }
  .headline {
    position: absolute;
    left: 106px;
    top: 72px;
    margin: 0;
    font-family: "Marcellus", serif;
    font-weight: 400;
    color: var(--cherry-red);
    font-size: 62px;
    line-height: 72px;
    letter-spacing: 1px;
  }
  .headline__small {
    font-size: 46px;
  }
  .facts {
    position: absolute;
    left: 112px;
    top: 236px;
    margin: 0;
    padding: 0;
    list-style: none;
    width: 400px;
  }
  .facts__item {
    position: relative;
    padding-left: 35px;
    margin-bottom: 14px;
    font-size: 18px;
    line-height: 23px;
    color: var(--ink);
  }
  .facts__item::before {
    content: "";
    position: absolute;
    left: 0;
    top: 4px;
    width: 14px;
    height: 14px;
    border-radius: 50%;
    background: var(--fruit-yellow);
    border: 1.5px solid var(--cherry-red);
  }
  .brand {
    position: absolute;
    left: 730px;
    top: 553px;
    width: 384px;
    height: 150px;
    display: flex;
    align-items: center;
    justify-content: center;
    gap: 14px;
  }
  .brand__dot {
    width: 34px;
    height: 34px;
    border-radius: 50%;
    background: var(--bowl-red);
  }
  .brand__name {
    font-family: "Lato", sans-serif;
    font-weight: 700;
    font-size: 34px;
    color: var(--bowl-red);
  }
  .contact {
    position: absolute;
    left: 88px;
    top: 707px;
    display: flex;
    align-items: baseline;
    gap: 30px;
    color: var(--paper);
  }
  .contact__web {
    font-weight: 700;
    font-size: 21px;
  }
  .contact__phone {
    font-size: 18px;
  }
</style>
</head>
<body>
<main class="card">
  <svg class="card__art" width="1200" height="765" viewBox="0 0 1200 765" aria-hidden="false">
    <defs>
      <radialGradient id="fruit" cx="40%" cy="35%" r="65%">
        <stop offset="0" stop-color="#fde7a0"/>
        <stop offset="0.55" stop-color="#f7cf5a"/>
        <stop offset="1" stop-color="#ef6a45"/>
      </radialGradient>
      <radialGradient id="bowl" cx="50%" cy="50%" r="55%">
        <stop offset="0" stop-color="#f5b548"/>
        <stop offset="0.6" stop-color="#ec5a35"/>
        <stop offset="1" stop-color="#9e1f14"/>
      </radialGradient>
      <linearGradient id="band" x1="0" y1="0" x2="0" y2="1">
        <stop offset="0" stop-color="#f26a3a"/>
        <stop offset="1" stop-color="#e2442a"/>
      </linearGradient>
    </defs>

    <!-- lower colour band -->
    <path class="band-line" d="M0 500 C 300 610, 560 665, 760 655 C 950 645, 1080 610, 1200 575" fill="none" stroke="#f26a3a" stroke-width="2"/>
    <path class="band" d="M0 512 C 300 625, 560 675, 760 665 C 950 655, 1080 620, 1200 585 L1200 765 L0 765 Z" fill="url(#band)"/>

    <!-- fruit photography areas -->
    <g role="img" aria-label="Single Rainier cherry, faded, top corner">
      <circle cx="58" cy="48" r="40" fill="url(#fruit)" opacity="0.35"/>
    </g>
    <g role="img" aria-label="Rainier cherry with stem">
      <circle cx="749" cy="160" r="45" fill="url(#fruit)"/>
    </g>
    <g role="img" aria-label="Rainier cherry with stem">
      <circle cx="677" cy="284" r="45" fill="url(#fruit)"/>
    </g>
    <g role="img" aria-label="Rainier cherry with stem">
      <circle cx="770" cy="396" r="42" fill="url(#fruit)"/>
    </g>
    <g role="img" aria-label="Rainier cherry with stem">
      <circle cx="558" cy="468" r="45" fill="url(#fruit)"/>
    </g>
    <g role="img" aria-label="Rainier cherry resting on the band">
      <circle cx="178" cy="605" r="42" fill="url(#fruit)"/>
    </g>
    <g role="img" aria-label="Red bowl filled with Rainier cherries">
      <ellipse cx="975" cy="322" rx="150" ry="148" fill="url(#bowl)"/>
    </g>

    <!-- brand oval -->
    <ellipse cx="922" cy="628" rx="196" ry="75" fill="#ffffff" stroke="#e8432c" stroke-width="4"/>
  </svg>

  <h1 class="headline">TASTE <span class="headline__small">THE</span><br>DIFFERENCE</h1>

  <ul class="facts">
    <li class="facts__item">Yellow cherries - yellow fruit (the blush on the skin is a kiss from the sun)</li>
    <li class="facts__item">Juice doesn't stain - Kid Friendly</li>
    <li class="facts__item">Add contrast to your summer table</li>
    <li class="facts__item">Sweetest Variety - still low glycemic</li>
    <li class="facts__item">Source of Vitamin C, Source of Potassium, and Source of Melatonin</li>
    <li class="facts__item">Rainiers take up to 4x as much work as red cherries</li>
  </ul>

  <div class="brand">
    <span class="brand__dot"></span>
    <span class="brand__name">Brightvale Cherries</span>
  </div>

  <footer class="contact">
    <span class="contact__web">www.brightvalecherries.com</span>
    <span class="contact__phone">Tel. 555.014.2837 | Fax. 555.014.2880</span>
  </footer>
</main>
</body>
</html>
```